The Verdant Ledger App - Modernization & Graphics User Interface Friendliness Updates

We are Verdant Ledger, and we want to bring a new branding look and graphical user interface to the Verdant Ledger App. The app is a quick reference encyclopedia for all things produce. Boasting articles on over 2,000 produce items, with information ranging from taste and application to geographical and cultural significance. Included in its features are over 10 thousand recipes, and the Verdant Ledger App Harvest Circle – a global initiative to connect farmer, customer, and chef in one sustainable and easy to use application. The design needs to bring a greater sense of social connection – encouraging the user to participate in the 'Harvest Circled' experience voluntarily. The design should reflect a sense of authority reflecting the authenticity and reliability of the provided information, it's writing, and its sources. Download the App here: vledgr.example/install

Target Market(s)

Women and Men between ages 21-55.

Industry/Entity Type

Education

Font styles to use
Serif
Sans Serif

Colors

Designer to choose colors to be used in the design.

Requirements
Must have
• An updated user interface, the intuitive usability of the app is currently non-existent. We are looking to reflect as the authority on produce. The app design must reflect a professional, user-friendly, up-to-date, and trustworthy feel.
Nice to have
• To incorporate the social draw of the Harvest Circle we would like to include on the home page "Social Bubbles" (think Pictoloop stories) which updates with shared photos of produce and their location.
Should not have
• An overly complicated theme, distracting or unprofessional colors, and images.

```html
<!DOCTYPE html>
<html lang="en">
<head>
<meta charset="utf-8">
<title>All Fruits – Verdant Ledger</title>
<link rel="stylesheet" href="https://fonts.googleapis.com/css2?family=Open+Sans:wght@400;600&family=Amatic+SC:wght@700&display=swap">
<style>
  :root {
    --green: #5a9e1f;
    --title-yellow: #e9e23a;
    --ink: #464646;
    --muted: #a9a9a9;
    --divider: #ececec;
    --chevron: #c4c4c4;
    --white: #ffffff;
  }
  * { margin: 0; padding: 0; box-sizing: border-box; }
  html, body { width: 675px; height: 1200px; overflow: hidden; background: var(--white); }
  body { font-family: "Open Sans", Arial, sans-serif; color: var(--ink); position: relative; }

  .screen { position: relative; width: 675px; height: 1200px; overflow: hidden; }

  .hero {
    position: absolute; left: 0; top: 0; width: 675px; height: 322px;
    background:
      radial-gradient(circle at 8% 75%, #c7284a 0, #a81f3c 18%, transparent 34%),
      radial-gradient(circle at 30% 18%, #f0a132 0, #e2882a 14%, transparent 28%),
      radial-gradient(circle at 22% 50%, #b92c2c 0, transparent 26%),
      radial-gradient(circle at 38% 60%, #4f7b2c 0, transparent 22%),
      linear-gradient(90deg, #7b3a2a 0%, #6f6a5e 45%, #9c968d 70%, #a9a49b 100%);
  }
  .hero::after {
    content: ""; position: absolute; inset: 0;
    background: linear-gradient(180deg, rgba(0,0,0,0.35) 0%, rgba(0,0,0,0) 22%);
  }

  .status-bar {
    position: absolute; left: 0; top: 0; width: 675px; height: 40px;
    color: var(--white); font-size: 22px; font-weight: 600;
  }
  .status-bar .time { position: absolute; left: 0; right: 0; top: 6px; text-align: center; }
  .status-bar .battery-text { position: absolute; right: 70px; top: 6px; }
  .status-bar svg { position: absolute; }

  .nav-icon { position: absolute; }

  .page-title {
    position: absolute; left: 370px; top: 112px;
    font-family: "Amatic SC", cursive; font-weight: 700; color: var(--title-yellow);
    line-height: 0.9;
  }
  .page-title .small { display: block; font-size: 40px; padding-left: 6px; }
  .page-title .large { display: block; font-size: 108px; letter-spacing: 2px; }

  .last-update { position: absolute; left: 368px; top: 264px; color: #2e2e2e; font-size: 18px; line-height: 1.2; }
  .last-update svg { position: absolute; left: 0; top: 8px; }
  .last-update .label { padding-left: 38px; font-weight: 600; display: block; }
  .last-update .date { padding-left: 38px; display: block; color: #3b3b3b; }

  .filter-button {
    position: absolute; left: 301px; top: 318px; width: 72px; height: 72px;
    border-radius: 50%; background: var(--green);
    box-shadow: 0 3px 8px rgba(0,0,0,0.2);
  }
  .filter-button svg { position: absolute; left: 18px; top: 18px; }

  .fruit-list { position: absolute; left: 0; top: 423px; width: 675px; list-style: none; }
  .fruit-item { position: relative; height: 180px; border-bottom: 2px solid var(--divider); margin: 0 38px; }
  .fruit-item .thumb {
    position: absolute; left: 0; top: 27px; width: 126px; height: 126px;
    background:
      radial-gradient(circle at 55% 60%, #2a2744 0, #35315a 30%, transparent 62%),
      linear-gradient(135deg, #6e9c42 0%, #4a6e2c 50%, #2f3d22 100%);
  }
  .fruit-item .name { position: absolute; left: 178px; top: 44px; font-size: 29px; font-weight: 600; color: var(--ink); white-space: nowrap; }
  .fruit-item .meta { position: absolute; left: 178px; top: 98px; font-size: 20px; color: var(--muted); display: flex; align-items: center; }
  .fruit-item .meta svg { margin-right: 10px; }
  .fruit-item .meta .likes { margin-left: 28px; display: flex; align-items: center; }
  .fruit-item .chevron { position: absolute; right: 0; top: 72px; }
  .fruit-item .favourite { position: absolute; right: 44px; top: 76px; }
</style>
</head>
<body>
<main class="screen">
  <div class="hero" role="img" aria-label="Photo of assorted fresh fruits – dragon fruit, strawberries, kiwi, cherries and orange – on grey wooden boards"></div>

  <div class="status-bar">
    <svg width="74" height="20" viewBox="0 0 74 20" style="left:14px;top:10px">
      <circle cx="5" cy="10" r="4" fill="#fff"/><circle cx="15" cy="10" r="4" fill="#fff"/>
      <circle cx="25" cy="10" r="4" fill="#fff"/><circle cx="35" cy="10" r="4" fill="#fff"/>
      <circle cx="45" cy="10" r="4" fill="none" stroke="#fff" stroke-width="1.5"/>
      <path d="M56 9 a11 11 0 0 1 16 0 M59 12 a7 7 0 0 1 10 0" stroke="#fff" stroke-width="2" fill="none"/>
      <circle cx="64" cy="16" r="2" fill="#fff"/>
    </svg>
    <span class="time">12:45 PM</span>
    <svg width="14" height="22" viewBox="0 0 14 22" style="right:150px;top:9px">
      <path d="M2 6 L12 16 L7 20 V2 L12 6 L2 16" stroke="#fff" stroke-width="2" fill="none"/>
    </svg>
    <span class="battery-text">100%</span>
    <svg width="52" height="22" viewBox="0 0 52 22" style="right:12px;top:9px">
      <rect x="1" y="2" width="44" height="18" rx="4" fill="none" stroke="#fff" stroke-width="2"/>
      <rect x="4" y="5" width="38" height="12" rx="2" fill="#fff"/>
      <rect x="47" y="8" width="4" height="6" rx="1" fill="#fff"/>
    </svg>
  </div>

  <svg class="nav-icon" width="30" height="34" viewBox="0 0 30 34" style="left:32px;top:86px" aria-label="Back">
    <path d="M22 3 L7 17 L22 31" stroke="#fff" stroke-width="4" fill="none" stroke-linecap="round" stroke-linejoin="round"/>
  </svg>
  <svg class="nav-icon" width="36" height="36" viewBox="0 0 36 36" style="left:576px;top:84px" aria-label="Search">
    <circle cx="15" cy="15" r="11" stroke="#fff" stroke-width="3" fill="none"/>
    <path d="M23 23 L33 33" stroke="#fff" stroke-width="3.5" stroke-linecap="round"/>
  </svg>
  <svg class="nav-icon" width="12" height="36" viewBox="0 0 12 36" style="left:634px;top:84px" aria-label="More options">
    <circle cx="6" cy="5" r="3.5" fill="#fff"/><circle cx="6" cy="18" r="3.5" fill="#fff"/><circle cx="6" cy="31" r="3.5" fill="#fff"/>
  </svg>

  <h1 class="page-title"><span class="small">All</span><span class="large">Fruits</span></h1>

  <div class="last-update">
    <svg width="28" height="28" viewBox="0 0 28 28">
      <rect x="2" y="4" width="24" height="22" rx="2" fill="none" stroke="#2e2e2e" stroke-width="2.4"/>
      <path d="M2 10 H26 M8 1 V7 M20 1 V7" stroke="#2e2e2e" stroke-width="2.4"/>
      <rect x="7" y="14" width="4" height="3" fill="#2e2e2e"/><rect x="14" y="14" width="4" height="3" fill="#2e2e2e"/>
      <rect x="7" y="19" width="4" height="3" fill="#2e2e2e"/>
    </svg>
    <span class="label">Last Update :</span>
    <span class="date">13 September 2017</span>
  </div>

  <div class="filter-button" aria-label="Filter">
    <svg width="36" height="36" viewBox="0 0 36 36">
      <path d="M3 11 H33 M3 25 H33" stroke="#fff" stroke-width="3" stroke-linecap="round"/>
      <circle cx="23" cy="11" r="4.5" fill="var(--green)" stroke="#fff" stroke-width="3"/>
      <circle cx="12" cy="25" r="4.5" fill="var(--green)" stroke="#fff" stroke-width="3"/>
    </svg>
  </div>

  <ul class="fruit-list">
    <li class="fruit-item">
      <div class="thumb" role="img" aria-label="Photo of Concord grape clusters on the vine"></div>
      <span class="name">Grapes Concord</span>
      <div class="meta">
        <svg width="26" height="16" viewBox="0 0 26 16"><path d="M1 8 Q13 -4 25 8 Q13 20 1 8 Z" fill="none" stroke="#b5b5b5" stroke-width="2"/><circle cx="13" cy="8" r="3.5" fill="#b5b5b5"/></svg>
        Views 2094
        <span class="likes"><svg width="20" height="18" viewBox="0 0 20 18"><path d="M10 16 L2.5 8.5 A4.5 4.5 0 0 1 10 3 A4.5 4.5 0 0 1 17.5 8.5 Z" fill="none" stroke="#b5b5b5" stroke-width="2"/></svg>Likes 294</span>
      </div>
      <svg class="chevron" width="20" height="34" viewBox="0 0 20 34"><path d="M3 3 L17 17 L3 31" stroke="var(--chevron)" stroke-width="3" fill="none"/></svg>
    </li>
    <li class="fruit-item">
      <div class="thumb" role="img" aria-label="Photo of seedless Concord grape clusters on the vine"></div>
      <span class="name">Grapes Concord Seedless</span>
      <div class="meta">
        <svg width="26" height="16" viewBox="0 0 26 16"><path d="M1 8 Q13 -4 25 8 Q13 20 1 8 Z" fill="none" stroke="#b5b5b5" stroke-width="2"/><circle cx="13" cy="8" r="3.5" fill="#b5b5b5"/></svg>
        Views 2094
        <span class="likes"><svg width="20" height="18" viewBox="0 0 20 18"><path d="M10 16 L2.5 8.5 A4.5 4.5 0 0 1 10 3 A4.5 4.5 0 0 1 17.5 8.5 Z" fill="none" stroke="#b5b5b5" stroke-width="2"/></svg>Likes 294</span>
      </div>
      <svg class="chevron" width="20" height="34" viewBox="0 0 20 34"><path d="M3 3 L17 17 L3 31" stroke="var(--chevron)" stroke-width="3" fill="none"/></svg>
    </li>
    <li class="fruit-item">
      <div class="thumb" role="img" aria-label="Photo of sweet green-vine grape clusters"></div>
      <span class="name">Grapes Sugar Cloud</span>
      <div class="meta">
        <svg width="26" height="16" viewBox="0 0 26 16"><path d="M1 8 Q13 -4 25 8 Q13 20 1 8 Z" fill="none" stroke="#b5b5b5" stroke-width="2"/><circle cx="13" cy="8" r="3.5" fill="#b5b5b5"/></svg>
        Views 2094
        <span class="likes"><svg width="20" height="18" viewBox="0 0 20 18"><path d="M10 16 L2.5 8.5 A4.5 4.5 0 0 1 10 3 A4.5 4.5 0 0 1 17.5 8.5 Z" fill="none" stroke="#b5b5b5" stroke-width="2"/></svg>Likes 294</span>
      </div>
      <svg class="chevron" width="20" height="34" viewBox="0 0 20 34"><path d="M3 3 L17 17 L3 31" stroke="var(--chevron)" stroke-width="3" fill="none"/></svg>
    </li>
    <li class="fruit-item">
      <div class="thumb" role="img" aria-label="Photo of Kyoho grape clusters on the vine"></div>
      <span class="name">Grapes Kyoho</span>
      <div class="meta">
        <svg width="26" height="16" viewBox="0 0 26 16"><path d="M1 8 Q13 -4 25 8 Q13 20 1 8 Z" fill="none" stroke="#b5b5b5" stroke-width="2"/><circle cx="13" cy="8" r="3.5" fill="#b5b5b5"/></svg>
        Views 2094
        <span class="likes"><svg width="20" height="18" viewBox="0 0 20 18"><path d="M10 16 L2.5 8.5 A4.5 4.5 0 0 1 10 3 A4.5 4.5 0 0 1 17.5 8.5 Z" fill="none" stroke="#b5b5b5" stroke-width="2"/></svg>Likes 294</span>
      </div>
      <svg class="favourite" width="34" height="30" viewBox="0 0 34 30" aria-label="Liked"><path d="M17 29 L3.5 15.5 A8 8 0 0 1 17 4.5 A8 8 0 0 1 30.5 15.5 Z" fill="var(--green)"/></svg>
      <svg class="chevron" width="20" height="34" viewBox="0 0 20 34"><path d="M3 3 L17 17 L3 31" stroke="var(--chevron)" stroke-width="3" fill="none"/></svg>
    </li>
  </ul>
</main>
</body>
</html>
```